VerintaCore PowerPoint Presentation Design

I am looking for a PowerPoint design for a new company based in Dallas, Texas called VerintaCore. We provide extremely powerful predictive and prescriptive analytics software focused on the Internet of Things (IoT) market. Our initial products are called VRC Foundry and VRC Pulse. We would like to see designs that support our logo design, which is attached.

I AM LOOKING FOR A THEME TO BE DEVELOPED FOR THE TITLE SLIDE AND INSIDE SLIDES OF A PRESENTATION. I AM NOT LOOKING FOR SOMEONE TO TAKE MY CONTENT AND CREATE A COMPLETE PRESENTATION.

Target Market(s)

Advanced Analytics, Internet of Things

Industry/Entity Type

It Company

Requirements
Must have
• Bolder colors, but they must work with the logo
Nice to have
• I prefer that the design incorporate the them of "connectivity" or "connectedness" to reflect the IoT market and "intelligence" or "smart" to reflect the analytics aspect of the business
Should not have
• I don't want people represented in the graphics scheme

```html
<!DOCTYPE html>
<html lang="en">
<head>
<meta charset="utf-8">
<title>VerintaCore – Table layouts</title>
<link href="https://fonts.googleapis.com/css2?family=Arimo:wght@400;700&display=swap" rel="stylesheet">
<style>
:root{
  --ink:#000000;
  --text:#262626;
  --muted:#404040;
  --brand-blue:#0a3cff;
  --brand-orange:#f5a000;
  --orange-light:#ffb820;
  --orange-dark:#e08a00;
  --row-shade:#d9d9d9;
  --rule:#c8c8c8;
  --bg:#ffffff;
}
*{box-sizing:border-box;margin:0;padding:0}
html,body{width:1200px;height:831px;overflow:hidden;background:var(--bg)}
body{position:relative;font-family:"Arimo",Arial,sans-serif;color:var(--text)}
.slide-title{position:absolute;left:23px;top:12px;font-size:34px;font-weight:700;color:var(--ink)}
.slide-subtitle{position:absolute;left:23px;top:60px;font-size:27px;color:var(--muted)}
.header-rule{position:absolute;left:0;top:107px;width:1200px;height:3px;
  background:linear-gradient(90deg,var(--brand-blue) 0%,rgba(10,60,255,.45) 40%,rgba(10,60,255,0) 100%)}
.brand{position:absolute;right:28px;top:28px;display:flex;align-items:center;gap:8px;
  font-size:27px;font-weight:700;color:var(--brand-blue)}
.brand-dot{width:12px;height:12px;border-radius:50%;background:var(--brand-orange)}
.block{position:absolute;width:563px}
.block.left{left:23px}
.block.right{left:611px}
.block-title{font-size:18px;font-weight:700;color:var(--ink)}
.block-title.underlined{height:36px;padding-top:8px;border-bottom:1.5px solid #9a8a70}
.block-title.banner{height:36px;padding:7px 12px;color:var(--ink);
  background:linear-gradient(180deg,var(--orange-light),var(--brand-orange) 60%,var(--orange-dark));
  box-shadow:0 2px 3px rgba(0,0,0,.25)}
table{width:100%;border-collapse:collapse;table-layout:fixed;font-size:15px}
col.c1{width:33%}col.c2{width:33%}col.c3{width:34%}
th,td{padding:0 6px;text-align:right;height:40px}
th:first-child,td:first-child{text-align:left}
th{font-weight:700}
.plain thead th{height:42px;border-bottom:1.5px solid var(--brand-orange)}
.plain tbody tr:nth-child(even) td{background:var(--row-shade)}
.plain tbody tr:last-child td{border-bottom:1.5px solid var(--brand-orange)}
.boxed{border:1.5px solid var(--brand-blue)}
.boxed thead th{background:var(--brand-blue);color:#fff;height:42px}
.boxed td{border-top:1px solid var(--rule)}
.boxed td+td{border-left:1px solid var(--rule)}
.compact td{height:39.5px}
.compact thead th{height:38px}
.footer-page{position:absolute;left:596px;top:798px;font-size:14px;color:var(--muted)}
.footer-label{position:absolute;right:28px;top:798px;font-size:14px;color:var(--muted)}
</style>
</head>
<body>
<h1 class="slide-title">Slide title</h1>
<p class="slide-subtitle">Subtitle</p>
<div class="brand"><span class="brand-dot"></span>VerintaCore</div>
<div class="header-rule"></div>

<section class="block left" style="top:123px">
  <h2 class="block-title underlined">Table option 1</h2>
  <table class="plain">
    <colgroup><col class="c1"><col class="c2"><col class="c3"></colgroup>
    <thead><tr><th>Table heading</th><th>Table heading</th><th>Table heading</th></tr></thead>
    <tbody>
      <tr><td>Table text</td><td>5</td><td>77</td></tr>
      <tr><td>Table text</td><td>26</td><td>66</td></tr>
      <tr><td>Table text</td><td>6</td><td>36</td></tr>
      <tr><td>Table text</td><td>3</td><td>9</td></tr>
      <tr><td>Table text</td><td>8</td><td>2</td></tr>
      <tr><td>Table text</td><td>3</td><td>83</td></tr>
    </tbody>
  </table>
</section>

<section class="block right" style="top:135px">
  <h2 class="block-title banner">Table option 1</h2>
  <table class="plain compact">
    <colgroup><col class="c1"><col class="c2"><col class="c3"></colgroup>
    <thead><tr><th>Table heading</th><th>Table heading</th><th>Table heading</th></tr></thead>
    <tbody>
      <tr><td>Table text</td><td>5</td><td>77</td></tr>
      <tr><td>Table text</td><td>26</td><td>66</td></tr>
      <tr><td>Table text</td><td>6</td><td>36</td></tr>
      <tr><td>Table text</td><td>3</td><td>9</td></tr>
      <tr><td>Table text</td><td>8</td><td>2</td></tr>
      <tr><td>Table text</td><td>3</td><td>83</td></tr>
    </tbody>
  </table>
</section>

<section class="block left" style="top:456px">
  <h2 class="block-title underlined" style="margin-bottom:4px">Table option 2</h2>
  <table class="boxed">
    <colgroup><col class="c1"><col class="c2"><col class="c3"></colgroup>
    <thead><tr><th>Table heading</th><th>Table heading</th><th>Table heading</th></tr></thead>
    <tbody>
      <tr><td>Table text</td><td>5</td><td>77</td></tr>
      <tr><td>Table text</td><td>26</td><td>66</td></tr>
      <tr><td>Table text</td><td>6</td><td>36</td></tr>
      <tr><td>Table text</td><td>3</td><td>9</td></tr>
      <tr><td>Table text</td><td>8</td><td>2</td></tr>
      <tr><td>Table text</td><td>3</td><td>83</td></tr>
    </tbody>
  </table>
</section>

<section class="block right" style="top:468px">
  <h2 class="block-title banner">Table option 2</h2>
  <table class="boxed compact">
    <colgroup><col class="c1"><col class="c2"><col class="c3"></colgroup>
    <thead><tr><th>Table heading</th><th>Table heading</th><th>Table heading</th></tr></thead>
    <tbody>
      <tr><td>Table text</td><td>5</td><td>77</td></tr>
      <tr><td>Table text</td><td>26</td><td>66</td></tr>
      <tr><td>Table text</td><td>6</td><td>36</td></tr>
      <tr><td>Table text</td><td>3</td><td>9</td></tr>
      <tr><td>Table text</td><td>8</td><td>2</td></tr>
      <tr><td>Table text</td><td>3</td><td>83</td></tr>
    </tbody>
  </table>
</section>

<div class="footer-page">4</div>
<div class="footer-label">INTERNAL</div>
</body>
</html>
```